Trvmlegal.com needs a wedsite. Law Office of Darnell P. Whitby

Darnell P. Whitby is a criminal law firm that is 5 years old. We have already had all the content written and now just need the website designed. We also just finished our logo design using Pixel Harbor and would like it used in the design of the website.

Industry/Entity Type

Law Firm

Number of Pages Required

5+ page

Requirements
Must have
• I was our new logo to be on the website also. I want Dallas sites as the stock pictures for the website. For example the Grey Stone Tribunal. I also need to be able to add YouTube videos. It has to adjust to be seen on computers and also cell phones. I need to be able to have a information sheet for clients to fill out and submit back to me.

```html
<!DOCTYPE html>
<html lang="en">
<head>
<meta charset="utf-8">
<title>Law Office of Darnell P. Whitby</title>
<link rel="stylesheet" href="https://fonts.googleapis.com/css2?family=Open+Sans:ital,wght@0,300;0,400;0,600;0,700;1,700;1,800&family=Gelasio:ital@1&family=Arimo:wght@400;700&display=swap">
<style>
:root{
  --navy:#0f2f6e;
  --navy-light:#2d4f8e;
  --blue-link:#1f5bb5;
  --badge:#2a62b8;
  --dark:#333333;
  --darker:#2b2b2b;
  --rule:#cfcfcf;
  --ink:#222222;
  --muted:#9a9a9a;
  --panel:#f0f0f0;
  --tab:#e6e6e6;
  --active:#1c2833;
  --white:#ffffff;
  --gold:#e0a11b;
}
*{margin:0;padding:0;box-sizing:border-box}
html,body{width:1200px;height:2927px;overflow:hidden}
body{position:relative;background:var(--white);font-family:"Arimo",Arial,sans-serif;color:var(--ink)}
.abs{position:absolute}

/* top bar */
.topbar{left:0;top:0;width:1200px;height:43px;background:var(--dark)}
.topbar .icon{top:10px;width:22px;height:22px}
.search{left:925px;top:8px;width:174px;height:27px;background:#f4f4f4;border-radius:3px;font:italic 10px "Open Sans",sans-serif;color:#666;padding:7px 9px}
.search svg{position:absolute;right:7px;top:5px}

/* nav */
.nav{left:0;top:43px;width:1200px;height:129px;background:var(--white)}
.nav a{position:absolute;top:58px;font:400 15px "Open Sans",sans-serif;color:#333;text-decoration:none}
.nav .home{left:156px;top:0;width:82px;height:129px;background:var(--navy);color:var(--white);padding-top:58px;text-align:center}
.brand{left:522px;top:40px;width:156px;height:156px;border-radius:50%;background:var(--white);border:6px solid var(--navy);display:flex;align-items:center;justify-content:center;text-align:center;font:700 15px/1.3 "Open Sans",sans-serif;color:var(--navy);padding:0 14px;z-index:3}

/* hero */
.hero{left:0;top:172px;width:1200px;height:570px;background:radial-gradient(ellipse at 75% 55%,#8a5a2c 0%,#5b3516 40%,#2e1a0a 100%)}
.hero-rule{left:0;top:742px;width:1200px;height:6px;background:var(--navy)}
.hero-title{left:121px;top:362px;font:italic 800 84px "Open Sans",sans-serif;color:var(--white);letter-spacing:1px}
.hero-sub{left:121px;top:456px;font:600 27px "Open Sans",sans-serif;color:var(--white)}
.arrow{top:404px;width:53px;height:53px;background:var(--navy)}
.dot{top:693px;width:18px;height:18px;border-radius:50%;background:var(--white)}

/* intro */
.intro-title{left:0;top:794px;width:1200px;text-align:center;font:600 39px "Open Sans",sans-serif;color:var(--navy)}
.intro-sub{left:0;top:850px;width:1200px;text-align:center;font:400 27px "Open Sans",sans-serif;color:var(--ink)}
.intro-text{left:100px;top:883px;width:1000px;text-align:center;font:14px/19px "Arimo",sans-serif;color:#444}
.btn{background:var(--navy);color:var(--white);font:400 17px "Open Sans",sans-serif;display:flex;align-items:center;justify-content:center;text-decoration:none}

/* grey section */
.panel{left:0;top:1069px;width:1200px;height:808px;background:var(--panel)}
.practice{left:98px;top:1137px;width:321px;height:361px;background:var(--tab);border:1px solid #dcdcdc}
.practice h3{font:italic 30px "Gelasio",Georgia,serif;color:#222;padding:25px 0 0 20px;height:75px;font-weight:400}
.practice li{list-style:none;height:39px;border-top:2px solid #f2f2f2;display:flex;align-items:center;padding-left:18px;font:italic 14px "Arimo",sans-serif;color:#333;background:#ebebeb}
.practice li.on{background:var(--active);color:var(--white)}
.practice li svg{margin-right:14px}
.lead-blue{font:700 14px/18px "Arimo",sans-serif;color:var(--blue-link)}
.body{font:13.5px/16.5px "Arimo",sans-serif;color:#444}
.serif-h{font:italic 40px "Gelasio",Georgia,serif;color:#111}
.serif-h2{font:italic 31px "Gelasio",Georgia,serif;color:#111}
.more{font:italic 18px "Gelasio",Georgia,serif;color:#111;display:flex;align-items:center;gap:10px}
.sub-h{font:700 14px "Arimo",sans-serif;color:var(--blue-link)}
.date{width:103px;height:37px;background:var(--badge);color:var(--white);font:13px "Arimo",sans-serif;display:flex;align-items:center;justify-content:center}

/* white columns */
.col-h{font:300 31px/32px "Open Sans",sans-serif;color:var(--navy-light)}
.video{left:98px;top:2062px;width:150px;height:150px;background:radial-gradient(circle at 50% 45%,#3f8be0 0%,#123c8a 45%,#050d26 100%);display:flex;align-items:center;justify-content:center}
.lt-title{font:300 21px/25px "Open Sans",sans-serif;color:var(--navy-light)}
.lt-text{font:13.5px/21px "Arimo",sans-serif;color:var(--muted)}
.day{font:300 38px "Open Sans",sans-serif;color:#444}
.month{font:300 20px "Open Sans",sans-serif;color:var(--navy-light)}
.faq{left:780px;top:2062px;width:322px}
.faq li{list-style:none;height:63px;display:flex;align-items:center;padding-left:22px;font:400 15px "Open Sans",sans-serif;color:#333;background:#f7f7f7}
.faq li:nth-child(even){background:#f0f0f0}
.faq li span{color:var(--gold);margin-right:18px;font-weight:700}

/* footer */
.footer{left:0;top:2532px;width:1200px;height:323px;background:var(--dark);border-top:5px solid var(--rule)}
.foot-title{left:0;top:2571px;width:1200px;text-align:center;font:400 33px "Open Sans",sans-serif;color:var(--white)}
.foot-text{left:210px;top:2628px;width:780px;text-align:center;font:14px/19px "Arimo",sans-serif;color:var(--white)}
.foot-line{font:14px "Arimo",sans-serif;color:var(--white)}
.bottombar{left:0;top:2855px;width:1200px;height:72px;background:var(--darker);border-top:3px solid #4a4a4a}
.copy{left:98px;top:2888px;font:13px "Arimo",sans-serif;color:var(--white)}
</style>
</head>
<body>

<header>
  <div class="abs topbar">
    <svg class="abs icon" style="left:98px" viewBox="0 0 22 22"><rect x="1" y="4" width="20" height="14" fill="#fff"/><path d="M1 4 11 12 21 4" fill="none" stroke="#333" stroke-width="2"/></svg>
    <svg class="abs icon" style="left:150px" viewBox="0 0 22 22"><circle cx="11" cy="11" r="8" fill="#fff"/></svg>
    <svg class="abs icon" style="left:200px" viewBox="0 0 22 22"><circle cx="11" cy="11" r="8" fill="#fff"/></svg>
    <svg class="abs icon" style="left:256px" viewBox="0 0 22 22"><rect x="5" y="1" width="12" height="20" rx="2" fill="none" stroke="#fff" stroke-width="2"/><circle cx="11" cy="17" r="1.3" fill="#fff"/></svg>
    <div class="abs search">Search . .
      <svg width="16" height="16" viewBox="0 0 16 16"><circle cx="6.5" cy="6.5" r="4.5" fill="none" stroke="#444" stroke-width="2"/><path d="M10 10 15 15" stroke="#444" stroke-width="2"/></svg>
    </div>
  </div>

  <nav class="abs nav">
    <a class="home" href="#">HOME</a>
    <a href="#" style="left:254px">ABOUT US</a>
    <a href="#" style="left:363px">CLIENTS</a>
    <a href="#" style="left:783px">PRACTICE</a>
    <a href="#" style="left:885px">BLOG</a>
    <a href="#" style="left:961px">CONTACTS</a>
  </nav>
  <div class="abs brand">Law Office of Darnell P. Whitby</div>
</header>

<section>
  <div class="abs hero" role="img" aria-label="Photo of brass scales of justice in a wood-panelled Dallas courtroom"></div>
  <div class="abs hero-rule"></div>
  <h1 class="abs hero-title">QUALIFIED</h1>
  <p class="abs hero-sub">PROFESSIONAL CRIMINAL DEFENSE</p>
  <div class="abs arrow" style="left:0"><svg width="53" height="53" viewBox="0 0 53 53"><path d="M31 17 21 26.5 31 36z" fill="#fff"/></svg></div>
  <div class="abs arrow" style="left:1147px"><svg width="53" height="53" viewBox="0 0 53 53"><path d="M22 17 32 26.5 22 36z" fill="#fff"/></svg></div>
  <div class="abs dot" style="left:569px;background:var(--badge)"></div>
  <div class="abs dot" style="left:590px"></div>
  <div class="abs dot" style="left:611px"></div>
</section>

<section>
  <h2 class="abs intro-title">NEED LEGAL ASSISTANCE?</h2>
  <h3 class="abs intro-sub">ASK OUR PROFESSIONALS</h3>
  <p class="abs intro-text">Praesent vestibulum aenean nonummy hendrerit mauris. Cum sociis natoque penatibus et magnis dis parturient montes ascetur ridiculus mus. Nulla dui. Fusce feugiat malesuada odio. Morbi nunc odio gravida at cursus nec luctus a lorem. Maecenas tristique orci ac sem. Duis ultricies pharetra magna. Donec accumsan malesuada orci. Donec sit amet eros.</p>
  <a class="abs btn" style="left:515px;top:960px;width:168px;height:55px" href="#">ASK NOW</a>
</section>

<section>
  <div class="abs panel"></div>
  <div class="abs practice">
    <h3>Practice</h3>
    <ul>
      <li class="on"><svg width="16" height="16" viewBox="0 0 16 16"><circle cx="8" cy="8" r="8" fill="#fff"/><path d="M4 8h7M8 5l3 3-3 3" stroke="#1c2833" stroke-width="1.6" fill="none"/></svg>Criminal Defense</li>
      <li><svg width="16" height="16" viewBox="0 0 16 16"><circle cx="8" cy="8" r="8" fill="#0f2f6e"/><path d="M4 8h7M8 5l3 3-3 3" stroke="#fff" stroke-width="1.6" fill="none"/></svg>DWI Defense</li>
      <li><svg width="16" height="16" viewBox="0 0 16 16"><circle cx="8" cy="8" r="8" fill="#0f2f6e"/><path d="M4 8h7M8 5l3 3-3 3" stroke="#fff" stroke-width="1.6" fill="none"/></svg>Drug Charges</li>
      <li><svg width="16" height="16" viewBox="0 0 16 16"><circle cx="8" cy="8" r="8" fill="#0f2f6e"/><path d="M4 8h7M8 5l3 3-3 3" stroke="#fff" stroke-width="1.6" fill="none"/></svg>Assault Cases</li>
      <li><svg width="16" height="16" viewBox="0 0 16 16"><circle cx="8" cy="8" r="8" fill="#0f2f6e"/><path d="M4 8h7M8 5l3 3-3 3" stroke="#fff" stroke-width="1.6" fill="none"/></svg>Theft Crimes</li>
      <li><svg width="16" height="16" viewBox="0 0 16 16"><circle cx="8" cy="8" r="8" fill="#0f2f6e"/><path d="M4 8h7M8 5l3 3-3 3" stroke="#fff" stroke-width="1.6" fill="none"/></svg>White Collar Crime</li>
      <li><svg width="16" height="16" viewBox="0 0 16 16"><circle cx="8" cy="8" r="8" fill="#0f2f6e"/><path d="M4 8h7M8 5l3 3-3 3" stroke="#fff" stroke-width="1.6" fill="none"/></svg>Juvenile Defense</li>
    </ul>
  </div>
  <p class="abs lead-blue" style="left:98px;top:1561px;width:300px">Lorem ipsum dolor sit amet, consectetuer adipiscing elit. Praesent vestibulum molestie lacus.</p>
  <p class="abs body" style="left:98px;top:1623px;width:320px">Aenean nonummy hendrerit mauris. Phasellus porta. Fusce suscipit varius mi. Cum sociis natoque penatibus et magnis dis parturient montes, nascetur ridiculus mus. Nulla dui. Fusce feugiat malesuada odio. Morbi nunc odio, gravida at, cursus nec, luctus a, lorem. Maecenas tristique orci ac sem. Duis ultricies pharetra magna. Donec accumsan malesuada orci. Donec sit amet eros. Lorem ipsum dolor sit amet, consectetuer adipiscing elit. Mauris fermentum dictum magna.</p>

  <h2 class="abs serif-h" style="left:472px;top:1124px">The Possibilities Are Endless</h2>
  <p class="abs" style="left:474px;top:1172px;font:italic 23px Gelasio,Georgia,serif;color:#222">Realize your constitutional right for qualified legal help</p>
  <p class="abs" style="left:474px;top:1232px;width:630px;font:700 13.5px/17px Arimo,sans-serif;color:#111">Lorem ipsum dolor sit amet, consectetur adipisicing elit, sed do eiusmod tempor incididunt labore et doloagna astum aliqua.</p>
  <p class="abs body" style="left:474px;top:1280px;width:630px">Uenim ad minim veniam, quis nostrud exercitation ullamco laboris nisi utaliquip ex ea commodoconsequat. Duis aute irurdolor into reprehenderitin voluptate velit esse cillum dolore eumo fugiat nlla pariatur. Excepteur sint occaecat cupidatat non proident, sunt in culpa qui officia deserunt mollit anim id est labo</p>
  <p class="abs more" style="left:474px;top:1392px"><svg width="18" height="18" viewBox="0 0 18 18"><circle cx="9" cy="9" r="9" fill="#111"/><path d="M7 5l4 4-4 4z" fill="#fff"/></svg>read more</p>

  <h2 class="abs serif-h2" style="left:474px;top:1443px">Who We Are?</h2>
  <p class="abs sub-h" style="left:474px;top:1502px">Personal Defense</p>
  <p class="abs body" style="left:474px;top:1518px;width:270px">massasoluta nobis est eligendi omnis voluasassumenda est, omnis dolore-sereeledusempquibusdamet aurerum odes perferendis doloribus asperiores repellat dolore</p>
  <p class="abs sub-h" style="left:474px;top:1662px">Business Defense</p>
  <p class="abs body" style="left:474px;top:1678px;width:270px">massasoluta nobis est eligendi omnis voluasassumenda est, omnis dolore-sereeledusempquibusdamet aurerum odes perferendis doloribus asperiores repellat dolore</p>
  <p class="abs more" style="left:474px;top:1801px"><svg width="18" height="18" viewBox="0 0 18 18"><circle cx="9" cy="9" r="9" fill="#111"/><path d="M7 5l4 4-4 4z" fill="#fff"/></svg>read more</p>

  <h2 class="abs serif-h2" style="left:767px;top:1443px">News &amp; Events</h2>
  <div class="abs date" style="left:767px;top:1514px">20/10/2011</div>
  <p class="abs body" style="left:767px;top:1568px;width:320px">Wed est lab orum eunam libero tempore, cum soluta nobis est ellenisa omnis volup ptas assu menda est, omnis doloresed repellendus &gt;&gt;</p>
  <div class="abs date" style="left:767px;top:1652px">12/10/2011</div>
  <p class="abs body" style="left:767px;top:1710px;width:320px">Amo est lab orum eunam libero temporecum soluta nobis est ellenisa omnis voluptas assu menda est, omnis doloresed repellendus &gt;&gt;</p>
  <p class="abs more" style="left:767px;top:1801px"><svg width="18" height="18" viewBox="0 0 18 18"><circle cx="9" cy="9" r="9" fill="#111"/><path d="M7 5l4 4-4 4z" fill="#fff"/></svg>archive</p>
</section>

<section>
  <h2 class="abs col-h" style="left:98px;top:1944px">SHORTLY<br>ABOUT US</h2>
  <h2 class="abs col-h" style="left:441px;top:1944px">LATEST<br>NEWS</h2>
  <h2 class="abs col-h" style="left:780px;top:1944px">AREAS OF<br>FAQ?</h2>

  <div class="abs video" role="img" aria-label="Firm introduction video showing scales of justice over a blue globe">
    <svg width="44" height="44" viewBox="0 0 44 44"><circle cx="22" cy="22" r="21" fill="rgba(0,0,0,.45)" stroke="#fff" stroke-width="2"/><path d="M17 13 31 22 17 31z" fill="#fff"/></svg>
  </div>
  <p class="abs lt-title" style="left:269px;top:2055px">OUR FIRM<br>ON VIDEO.</p>
  <p class="abs lt-text" style="left:269px;top:2110px;width:150px">Nam justo ante, hen drerit vitae aliqu condi mentum, commo dolo eu mitiam sol licit.</p>
  <p class="abs lt-text" style="left:98px;top:2222px;width:320px">Nam justo ante, hendrerit vitae aliquet condime ntum, com modo eu mi. Etiam sol licitudin odio at vehicula venenatis.</p>
  <p class="abs lt-text" style="left:98px;top:2306px;width:320px">Nam justo ante, hendrerit vitae aliquet condime ntum, com modo eu mi. Etiam sol licitudin odio at vehicula venenatis. Aenean ac pulvinar nisi. Donec sed posuere velit. Morbi eget massa sit amet ligula sagittis tempus sit amet.</p>

  <div class="abs day" style="left:448px;top:2050px">19</div><div class="abs month" style="left:448px;top:2098px">MAY</div>
  <p class="abs lt-title" style="left:527px;top:2053px">INEN DOLOR IPSUM.</p>
  <p class="abs lt-text" style="left:527px;top:2085px;width:240px">Nam justo ante, hendrerit vialiquet condimentum, commodo eutiam so licitudin odio vehicula venenatis.</p>
  <div class="abs day" style="left:448px;top:2190px">22</div><div class="abs month" style="left:448px;top:2238px">MAY</div>
  <p class="abs lt-title" style="left:527px;top:2193px">INEN DOLOR IPSUM.</p>
  <p class="abs lt-text" style="left:527px;top:2225px;width:240px">Nam justo ante, hendrerit vialiquet condimentum, commodo eutiam so licitudin odio vehicula venenatis.</p>
  <div class="abs day" style="left:448px;top:2330px">25</div><div class="abs month" style="left:448px;top:2378px">MAY</div>
  <p class="abs lt-title" style="left:527px;top:2333px">INEN DOLOR IPSUM.</p>
  <p class="abs lt-text" style="left:527px;top:2365px;width:240px">Nam justo ante, hendrerit vialiquet condimentum, commodo eutiam so licitudin odio vehicula venenatis.</p>

  <ul class="abs faq">
    <li><span>&gt;</span>ARREST &amp; BAIL BONDS</li>
    <li><span>&gt;</span>GRAND JURY PROCEEDINGS</li>
    <li><span>&gt;</span>PLEA AGREEMENTS</li>
    <li><span>&gt;</span>EXPUNCTION OF RECORDS</li>
    <li><span>&gt;</span>PROBATION RIGHTS</li>
    <li><span>&gt;</span>APPEALS AND WRITS</li>
  </ul>
</section>

<footer>
  <div class="abs footer"></div>
  <h2 class="abs foot-title">Contact Me</h2>
  <p class="abs foot-text">Lorem ipsum dolor sit amet, consectetuer adipiscing elit. Praesent vestibulum m olestie lacus. Aenean nonummy hendrerit mauris. Phasellus porta. Fusce suscipit varius mi. Lorem ipsum dolor sit amet, consectetuer adipiscing elit. Praesent vestibulum molestie lacus. Morbi nunc odio, gravida at, cursus neca</p>
  <p class="abs foot-line" style="left:0;top:2704px;width:1200px;text-align:center">PO Box 4471 Dallas TX 75201</p>
  <p class="abs foot-line" style="left:336px;top:2730px">Telephone: (214) 555-0148</p>
  <p class="abs foot-line" style="left:587px;top:2730px">E-mail: hello@trvmlegal.com</p>
  <a class="abs btn" style="left:492px;top:2784px;width:218px;height:47px;font-size:15px" href="#">CLIENT INTAKE FORM</a>
  <div class="abs bottombar"></div>
  <p class="abs copy">Copyright © 2015 - All Rights Reserved</p>
  <svg class="abs" style="left:913px;top:2882px" width="24" height="22" viewBox="0 0 22 22"><rect x="1" y="4" width="20" height="14" fill="#fff"/><path d="M1 4 11 12 21 4" fill="none" stroke="#2b2b2b" stroke-width="2"/></svg>
  <svg class="abs" style="left:966px;top:2882px" width="22" height="22" viewBox="0 0 22 22"><circle cx="11" cy="11" r="8" fill="#fff"/></svg>
  <svg class="abs" style="left:1017px;top:2882px" width="22" height="22" viewBox="0 0 22 22"><circle cx="11" cy="11" r="8" fill="#fff"/></svg>
  <svg class="abs" style="left:1070px;top:2880px" width="22" height="26" viewBox="0 0 22 26"><rect x="5" y="1" width="12" height="24" rx="2" fill="none" stroke="#fff" stroke-width="2"/><circle cx="11" cy="20" r="1.4" fill="#fff"/></svg>
</footer>

</body>
</html>
```